Marn-ridge Tide Harbor Custom Brokers Limited

Name: Dorvella Hastings
Title: Customs Broker
Address: Shop 9 Birchfield Commercial Complex
207-209 Harlow Road
Kingston 8
Telephone: (876)
Email: tideharborport@quillmail.example

```html
<!DOCTYPE html>
<html lang="en">
<head>
<meta charset="utf-8">
<title>Marn-ridge Tide Harbor Custom Brokers Limited – Business Card</title>
<link href="https://fonts.googleapis.com/css2?family=Montserrat:wght@500;600;700&family=Lato:wght@400&display=swap" rel="stylesheet">
<style>
  :root {
    --backdrop: #1f1f21;
    --navy: #132c54;
    --gold: #f0a824;
    --white: #ffffff;
  }
  * { margin: 0; padding: 0; box-sizing: border-box; }
  html, body {
    width: 1200px; height: 970px; overflow: hidden;
    background: var(--backdrop);
  }
  .canvas {
    position: relative; width: 1200px; height: 970px;
  }
  .card {
    position: absolute; left: 250px; width: 700px; height: 400px;
    background: var(--navy);
    box-shadow: 0 10px 30px rgba(0,0,0,.45);
  }
  .card--front { top: 60px; border-bottom: 6px solid var(--gold); }
  .card--back { top: 500px; }

  .brand {
    position: absolute; inset: 0;
    display: flex; flex-direction: column; align-items: center; justify-content: center;
    gap: 14px; text-align: center;
  }
  .brand__mark {
    width: 46px; height: 46px; border-radius: 50%; background: var(--gold);
  }
  .brand__name {
    font-family: "Montserrat", sans-serif; font-weight: 600;
    color: var(--white); font-size: 30px; letter-spacing: 1px; line-height: 1.25;
    text-transform: uppercase;
  }
  .brand__sub {
    font-family: "Montserrat", sans-serif; font-weight: 600;
    color: var(--white); font-size: 17px; letter-spacing: 6px;
  }

  .person {
    position: absolute; left: 70px; top: 170px; width: 300px; text-align: right;
  }
  .person__name {
    font-family: "Montserrat", sans-serif; font-weight: 700;
    color: var(--gold); font-size: 34px; line-height: 1.1;
  }
  .person__title {
    font-family: "Lato", sans-serif; color: var(--white); font-size: 17px; margin-top: 6px;
  }
  .divider {
    position: absolute; left: 398px; top: 130px; width: 2px; height: 140px; background: var(--gold);
  }
  .contact {
    position: absolute; left: 425px; top: 128px;
    font-family: "Lato", sans-serif; color: var(--white); font-size: 14px; line-height: 1.45;
  }
  .contact__row { display: flex; align-items: center; gap: 10px; margin-top: 6px; }
  .contact__icon { width: 16px; height: 16px; flex: none; }
</style>
</head>
<body>
<main class="canvas">
  <section class="card card--front" aria-label="Card front">
    <div class="brand">
      <span class="brand__mark" aria-hidden="true"></span>
      <p class="brand__name">Marn-ridge Tide Harbor</p>
      <p class="brand__sub">Custom Brokers Ltd.</p>
    </div>
  </section>

  <section class="card card--back" aria-label="Card back">
    <div class="person">
      <p class="person__name">Dorvella Hastings</p>
      <p class="person__title">Customs Broker</p>
    </div>
    <span class="divider" aria-hidden="true"></span>
    <address class="contact" style="font-style:normal">
      <p>Shop 9 Birchfield Commercial Complex<br>207-209 Harlow Road<br>Kingston 8</p>
      <p class="contact__row">
        <svg class="contact__icon" viewBox="0 0 24 24" aria-hidden="true"><path fill="#f0a824" d="M6.6 10.8a15.1 15.1 0 0 0 6.6 6.6l2.2-2.2a1 1 0 0 1 1-.25 11.4 11.4 0 0 0 3.6.57 1 1 0 0 1 1 1V20a1 1 0 0 1-1 1A17 17 0 0 1 3 4a1 1 0 0 1 1-1h3.5a1 1 0 0 1 1 1c0 1.25.2 2.45.57 3.57a1 1 0 0 1-.25 1z"/></svg>
        (876) 555 0142
      </p>
      <p class="contact__row">
        <svg class="contact__icon" viewBox="0 0 24 24" aria-hidden="true"><path fill="#f0a824" d="M2 5h20v14H2z"/><path fill="none" stroke="#132c54" stroke-width="1.8" d="M2 5l10 8 10-8M2 19l7-7M22 19l-7-7"/></svg>
        tideharborport@quillmail.example
      </p>
    </address>
  </section>
</main>
</body>
</html>
```